We require a professional design for a Cosmetic Surgery college. We have just submitted the request for our new logo which will be used on this card. We are the leaders in our field of education in Australia and this should be reflected in the quality of the card. People want to come and study with us because we are so outstanding in the field. Studying with us provides credibility, quality and courage.
Updates

Project Deadline Extended
Reason: Require updated logo to be used in design

Target Market(s)

25 - 40 year old professional women primarily from a medical background wanting to continue study in the cosmetic medical field, western speaking countries. The course average cost is 17k AU for 16 weeks.

Industry/Entity Type

Education

Requirements
Must have
• Must us the logo that is currently under design by this company.
Nice to have
• A medical twist very subtle would be nice possilbly rod of Asclepius.
Should not have
• Should not look old, we are dealing with modern medical concepts.
The logo that is being redesigned 3d silver, the attached logo is the old one.

```html
<!DOCTYPE html>
<html lang="en">
<head>
<meta charset="utf-8">
<title>Lumara business card</title>
<link href="https://fonts.googleapis.com/css2?family=Source+Sans+3:wght@400;600;700&display=swap" rel="stylesheet">
<style>
  :root {
    --teal: #1b9bb3;
    --teal-deep: #0f7d93;
    --teal-light: #3fb6cb;
    --white: #ffffff;
    --band: #d9eef2;
    --silver: #dfe6e8;
    --ink-soft: #5aa9b8;
    --stage: #e8e5df;
  }
  * { margin: 0; padding: 0; box-sizing: border-box; }
  html, body {
    width: 1200px; height: 1023px; overflow: hidden;
    background: var(--stage);
    font-family: "Source Sans 3", sans-serif;
  }
  .canvas { position: relative; width: 1200px; height: 1023px; }

  .card {
    position: absolute; width: 560px; height: 320px;
    border-radius: 26px; overflow: hidden;
    box-shadow: 0 10px 28px rgba(0,0,0,.18);
  }
  .card-front { left: 40px; top: 190px; background: var(--white); }
  .card-back {
    left: 610px; top: 500px;
    background: linear-gradient(135deg, var(--teal-deep), var(--teal) 55%, var(--teal-light));
  }
  .card-shapes { position: absolute; inset: 0; width: 100%; height: 100%; }

  .brand { position: absolute; display: flex; align-items: center; gap: 10px; white-space: nowrap; }
  .brand-dot { width: 40px; height: 40px; border-radius: 50%; background: var(--teal); flex: none; }
  .brand-name {
    font-weight: 600; font-size: 44px; line-height: 1; letter-spacing: 2px;
    color: var(--teal); text-transform: uppercase;
  }
  .brand-tagline {
    font-weight: 600; font-size: 9.5px; letter-spacing: 3.2px;
    color: var(--ink-soft); text-transform: uppercase; margin-top: 3px;
  }
  .card-front .brand { left: 30px; top: 34px; }

  .card-back .brand { left: 50%; top: 50%; transform: translate(-50%, -50%); }
  .card-back .brand-dot { background: var(--silver); width: 46px; height: 46px; }
  .card-back .brand-name { color: var(--silver); font-size: 50px; }
  .card-back .brand-tagline { color: var(--silver); font-size: 10px; letter-spacing: 3px; }

  .contact-block { position: absolute; left: 30px; top: 150px; color: var(--white); }
  .person { font-size: 19px; font-weight: 700; margin-bottom: 6px; line-height: 24px; }
  .person .role { font-weight: 400; font-size: 15px; }
  .contact-list { list-style: none; font-size: 12.5px; line-height: 17px; }
  .contact-list li { display: flex; align-items: center; gap: 8px; }
  .contact-list svg { width: 11px; height: 11px; flex: none; }

  .divider { position: absolute; left: 30px; right: 30px; top: 262px; height: 1px; background: rgba(255,255,255,.6); }
  .address { position: absolute; left: 30px; top: 268px; color: var(--white); font-size: 12.5px; line-height: 16px; }
</style>
</head>
<body>
<main class="canvas">

  <section class="card card-front">
    <svg class="card-shapes" viewBox="0 0 560 320" aria-hidden="true">
      <path d="M0 126 L230 126 C330 126 420 60 560 0 L560 320 L0 320 Z" fill="var(--band)"/>
      <path d="M0 138 L236 138 C338 138 428 74 560 14 L560 320 L0 320 Z" fill="var(--teal)"/>
      <path d="M236 138 C338 138 428 74 560 14" stroke="rgba(255,255,255,.7)" stroke-width="1.2" fill="none"/>
    </svg>

    <div class="brand">
      <span class="brand-dot"></span>
      <div>
        <div class="brand-name">Lumara</div>
        <div class="brand-tagline">Medical Aesthetics Education</div>
      </div>
    </div>

    <div class="contact-block">
      <p class="person">Harper Quinn <span class="role">| Director</span></p>
      <ul class="contact-list">
        <li><svg viewBox="0 0 12 12"><rect width="12" height="12" rx="2" fill="rgba(255,255,255,.35)"/><path d="M4 3 L5 5 L4.5 6 Q6 8 7 7.5 L9 8.5 L8.5 9.5 Q5 10 3 5 Z" fill="#fff"/></svg>07 55 500 118</li>
        <li><svg viewBox="0 0 12 12"><rect width="12" height="12" rx="2" fill="rgba(255,255,255,.35)"/><rect x="3" y="4" width="6" height="5" fill="#fff"/><rect x="4" y="2.5" width="4" height="2" fill="#fff"/></svg>07 55 500 119</li>
        <li><svg viewBox="0 0 12 12"><rect width="12" height="12" rx="2" fill="rgba(255,255,255,.35)"/><rect x="2.5" y="3.5" width="7" height="5" fill="#fff"/><path d="M2.5 3.5 L6 6.5 L9.5 3.5" stroke="#1b9bb3" fill="none" stroke-width=".8"/></svg>harper@lumara.edu.au</li>
        <li><svg viewBox="0 0 12 12"><rect width="12" height="12" rx="2" fill="rgba(255,255,255,.35)"/><circle cx="6" cy="6" r="3.5" fill="none" stroke="#fff"/><path d="M2.5 6 H9.5 M6 2.5 V9.5" stroke="#fff" stroke-width=".7"/></svg>www.Lumara.edu.au</li>
      </ul>
    </div>

    <div class="divider"></div>
    <p class="address">P.O Box 118 Harbourview Qld 4000<br>Level 2, Ten Marina Lane Harbourview Qld 4000</p>
  </section>

  <section class="card card-back">
    <svg class="card-shapes" viewBox="0 0 560 320" aria-hidden="true">
      <path d="M-20 300 C160 200 400 190 600 260" stroke="rgba(255,255,255,.07)" stroke-width="36" fill="none"/>
    </svg>
    <div class="brand">
      <span class="brand-dot"></span>
      <div>
        <div class="brand-name">Lumara</div>
        <div class="brand-tagline">Medical Aesthetics Education</div>
      </div>
    </div>
  </section>

</main>
</body>
</html>
```